Social Media Advert for Office Fruit Delivery in Dubai

We need an attractive design for social media adverts, for delivering assorted fruit boxes to companies. We will be delivering costume package fruit boxes, with great price, and great quality. Our fruit boxes is +4.5 kg and includes apples, bananas, kiwis, some citrus, and some stone fruit depending on seasonality. Our offer prices are AED 45, which is very competitive as we are wholesalers, and growers of some of our fruits. Our goal is to support health initiative set by responsible companies. Our delivery is free for companies who enrol into weekly delivery programs restricted to Dubai only. We suggest deliveries to be once a week, as our fruit is fresh, and great for consumption in a one week window. Considering each employee on average would consume two pieces of fruits a day, our fruit boxes is ideal for 4 employees in one working week. We need a talented designer, to kick start our sales. You can find more details about this project, and about our company on our website www.lunagrove.co follow us on social media @lunagroveuae

Target Market(s)

age 22-50, based in Dubai working individuals in companies with responsibility to care for it's employees and their health.

Font styles to use
Other font styles liked:
• IYC Avant Garde Gothic LT Bold

Colors

Designer to choose colors to be used in the design.

Requirements
Must have
• - Logo
• - offer price and product
Nice to have
• Check out the 'inspire' in attachments to understand what we are looking for

```html
<!DOCTYPE html>
<html lang="en">
<head>
<meta charset="utf-8">
<title>Luna Grove – Farm Fresh On Your Desk</title>
<link rel="stylesheet" href="https://fonts.googleapis.com/css2?family=Questrial&family=Saira+Condensed:wght@700;800&display=swap">
<style>
  :root{
    --stage:#3a3a3c;
    --lemon:#f5ef86;
    --orange:#e8643a;
    --ink:#2b2a24;
    --leaf-dark:#3d6a2c;
    --leaf:#6aa63d;
    --sky:#c9dceb;
  }
  *{box-sizing:border-box;margin:0;padding:0}
  html,body{width:1200px;height:800px;overflow:hidden}
  body{background:var(--stage);font-family:"Questrial",sans-serif;color:var(--ink)}
  .flyer{position:absolute;left:324px;top:10px;width:552px;height:780px;background:var(--lemon);overflow:hidden}
  .flyer-art{position:absolute;left:0;top:0}
  .abs{position:absolute}
  .brand-name{left:82px;top:31px;width:77px;text-align:center;font-size:15px;color:var(--orange);line-height:1.05}
  .brand-tag{left:64px;top:104px;width:113px;text-align:center;color:var(--orange);font-size:12px;letter-spacing:.5px;line-height:1.05}
  .brand-tag small{display:block;font-size:9.5px;letter-spacing:1px}
  .headline{left:236px;top:362px;width:310px;text-align:center;font-family:"Saira Condensed",sans-serif;font-weight:800;font-size:21px;letter-spacing:2px;color:var(--orange)}
  .intro{left:236px;top:394px;width:310px;text-align:center;font-size:9.3px;line-height:1.5;text-transform:uppercase}
  .hl{color:var(--orange)}
  .step{position:absolute;top:536px;width:164px;text-align:center}
  .step h3{font-family:"Questrial",sans-serif;font-weight:400;font-size:10.5px;letter-spacing:.6px;white-space:nowrap;color:var(--orange);padding-bottom:4px;border-bottom:1px solid var(--orange);margin:0 4px 6px}
  .step p{font-size:6.8px;line-height:1.6;text-transform:uppercase}
  .step p.big{font-size:7.6px}
  .step .accent{color:var(--orange);font-size:10px}
  .social{left:0;top:638px;width:552px;text-align:center;font-size:11px;letter-spacing:.5px}
  .social .dot{display:inline-block;width:9px;height:9px;border-radius:50%;background:var(--orange);vertical-align:-1px;margin-right:6px}
  .footer-line{left:0;width:552px;display:flex;justify-content:center;align-items:center;font-size:11.5px;letter-spacing:.4px;white-space:nowrap}
  .contact{top:724px}
  .address{top:750px;text-transform:uppercase;letter-spacing:.6px}
  .footer-line .item{display:inline-flex;align-items:center;gap:9px}
  .footer-line svg{display:block;flex:none}
  .sep{color:var(--orange);margin:0 10px}
</style>
</head>
<body>
<div class="flyer">
  <svg class="flyer-art" width="552" height="780" viewBox="0 0 552 780">
    <defs>
      <linearGradient id="orchard" x1="0" y1="0" x2="0" y2="1">
        <stop offset="0" stop-color="var(--sky)"/>
        <stop offset=".35" stop-color="var(--leaf-dark)"/>
        <stop offset=".7" stop-color="#4d7d33"/>
        <stop offset="1" stop-color="var(--leaf)"/>
      </linearGradient>
      <radialGradient id="fruitGlow" cx=".65" cy=".55" r=".4">
        <stop offset="0" stop-color="#e8742e" stop-opacity=".85"/>
        <stop offset="1" stop-color="#e8742e" stop-opacity="0"/>
      </radialGradient>
    </defs>

    <g role="img" aria-label="Photo of ripe tangerines hanging in an orchard">
      <path d="M0 0H552V225C440 290 340 320 230 322C140 322 60 292 0 250Z" fill="url(#orchard)"/>
      <path d="M0 0H552V225C440 290 340 320 230 322C140 322 60 292 0 250Z" fill="url(#fruitGlow)"/>
    </g>
    <path d="M0 302H22V318H0Z" fill="var(--orange)"/>
    <path d="M240 330C360 325 470 290 552 222V244C470 305 360 345 240 350Z" fill="var(--orange)"/>

    <circle cx="127" cy="346" r="104" fill="var(--lemon)"/>
    <path d="M30 380A100 100 0 0 0 224 380" fill="none" stroke="var(--orange)" stroke-width="4"/>
    <g role="img" aria-label="Photo of a delivery truck with a fruit-print wrap beside a tangerine tree">
      <circle cx="127" cy="346" r="94" fill="url(#orchard)"/>
      <circle cx="127" cy="346" r="94" fill="url(#fruitGlow)"/>
    </g>

    <path d="M64 0H177V156L120.5 136 64 156Z" fill="var(--orange)"/>
    <circle cx="120.5" cy="46" r="38" fill="var(--lemon)"/>
    <path d="M70 96H171V140L120.5 124 70 140Z" fill="var(--lemon)"/>

    <g fill="none" stroke="var(--orange)" stroke-width="2">
      <circle cx="97" cy="499" r="27"/>
      <circle cx="268" cy="499" r="27"/>
      <circle cx="456" cy="499" r="27"/>
      <path d="M82 488h5l5 16h14l3-11H89"/>
      <circle cx="94" cy="509" r="2"/><circle cx="104" cy="509" r="2"/>
    </g>
    <g fill="var(--orange)">
      <path d="M254 490c6-5 22-5 28 0v4h-7v-3h-14v3h-7z"/>
      <rect x="258" y="496" width="20" height="14" rx="2"/>
      <rect x="439" y="490" width="21" height="15"/>
      <path d="M461 495h7l5 6v4h-12z"/>
      <circle cx="445" cy="507" r="3"/><circle cx="467" cy="507" r="3"/>
    </g>

    <g fill="none" stroke="var(--orange)" stroke-width="1.5">
      <circle cx="210" cy="691" r="22"/>
      <circle cx="275" cy="691" r="22"/>
      <circle cx="341" cy="691" r="22"/>
    </g>
  </svg>

  <div class="abs brand-name">Luna<br>Grove</div>
  <div class="abs brand-tag">FARM FRESH<small>ON YOUR DESK</small></div>

  <h1 class="abs headline">FARM FRESH ON YOUR DESK</h1>
  <p class="abs intro">We are bringing from <span class="hl">fresh fruits</span> right to your office.<br>Create your own custom crate or we'll hand select<br>the best flavors in one convenient box!</p>

  <div class="step" style="left:15px">
    <h3>FIND YOUR FAVORITES ...</h3>
    <p>You can plan a combination of<br>fruits depending on your preference or<br>you can choose our best selling assorted<br>box of fruits AED 45.00 (net wt 4.5kg)</p>
  </div>
  <div class="step" style="left:186px">
    <h3>PLACE YOUR ORDER ....</h3>
    <p class="big">Call us directly<br><span class="accent">+971 4 555 0182</span> or visit<br>our online store at<br><span class="hl">www.lunagrove.co/fruitdelivery</span></p>
  </div>
  <div class="step" style="left:374px">
    <h3>W'LL BRING IT TO YOU ...</h3>
    <p class="big">Get your fruits package within<br><span class="accent">30 MINUTES</span> after your order<br>free delivery!</p>
  </div>

  <div class="abs social"><span class="dot"></span>@LUNAGROVEUAE</div>

  <div class="abs footer-line contact">
    <span class="item">
      <svg width="16" height="16" viewBox="0 0 16 16"><path fill="var(--orange)" d="M2 1c2-2 4-1 5 1l1 3c0 1-1 2-2 2 1 3 3 5 6 6 0-1 1-2 2-2l2 1c1 1 1 3-1 4C9 18-2 6 2 1z"/></svg>
      +971 4 555 0182
    </span>
    <span class="sep">|</span>
    <span class="item">
      <svg width="13" height="13" viewBox="0 0 13 13"><circle cx="6.5" cy="6.5" r="6.5" fill="var(--orange)"/></svg>
      WWW.LUNAGROVE.CO
    </span>
    <span class="sep">|</span>
    <span class="item">
      <svg width="16" height="12" viewBox="0 0 16 12"><rect width="16" height="12" rx="1" fill="var(--orange)"/><path d="M1 1l7 5 7-5" fill="none" stroke="var(--lemon)" stroke-width="1.2"/></svg>
      INFO@LUNAGROVE.CO
    </span>
  </div>
  <div class="abs footer-line address">
    <span class="item">
      <svg width="16" height="18" viewBox="0 0 16 18"><path fill="var(--orange)" d="M2 6a6 6 0 0 1 12 0c0 4-6 9-6 9S2 10 2 6z"/><circle cx="8" cy="6" r="2" fill="var(--lemon)"/><ellipse cx="8" cy="16" rx="7" ry="1.6" fill="none" stroke="var(--orange)" stroke-width="1.2"/></svg>
      Palm Row Market , Warehouse 12 &amp; 14 , Dubai , UAE
    </span>
  </div>
</div>
</body>
</html>
```